Bright Path Flyer Design for Virtual Online Clinic. -5.5 x 8.5 inches (half sheet)

We need a clean, modern flyer design for Bright Path, a new virtual walk-in clinic based in British Columbia. The flyer will be used in libraries, pharmacies, and community centers to help residents easily access primary care through their Bright Path NFC access card.
The flyer will ask a question : NEED A DOCTOR? This should be large and attention grabbing.
The design should clearly feature a Bright Path card image (the access card) as the centerpiece and visually show how patients can use it to book appointments. The tone should feel trustworthy, healthcare-oriented, and community-friendly — clean fonts, clear spacing, and strong readability from a distance.

Side One: This card has the NFC Access Card.
NEED A DOCTOR? (Large Font, Attention Grabbing)
How to Book an Appointment using your Bright Path Card
Step 1: Tap Your Card on Your Phone
Hold your card near the back of your phone.
It will activate automatically — no app needed.
The Bright Path scheduler will open.
Step 2: Schedule Your Appointment
Select your clinical concern.
Choose your time window.
Register (only once).
Confirm your appointment.
Step 3: Relax, we’ll take care of the rest
A doctor will call during your scheduled time.
Once booked, you’ll be able to call our office.
No emails, no texts — just a real person.
It’s that simple.
Side Two:
About Bright Path
Created by Dr. Marcus Ferrigan
Bright Path was founded to make healthcare simple and convenient. Prescription renewals. Common infections. Medical notes. And so much more.
Our doctors can address 120+ health concerns virtually — providing quality care without the waiting room. No waiting rooms. Just real doctors providing real care.
Why Patients Choose Bright Path
Easy access – book and be seen from anywhere in BC.
Effortless booking – tap your Bright Path Card to begin.
Trusted physicians – every visit is with a licensed BC family doctor.
How It Works
Book your visit — choose a time window that fits your day.
Join the queue — you’ll be called when it’s your turn.
Speak directly with your doctor — simple, secure, and stress-free.
Convenient Care for Common Concerns

Additional Details.
Please find the domain to be launched soon. I've attached the NFC card file for review, it is 85.5 mm x 54 mm. The card will be glued to the flyer.
I've attached examples of flyers but they are not the look I am seeking and I am looking for creative solutions.
Thank you!
http://brightpath-example.test/

Adult Patients in British Columbia

Healthcare

• Looking for clean lines, uniform appearance, and high legibility i.e poppins

0054AA
0677BA
7BADD7
CADEEF
E8F1F8

• Need A Doctor?
• Elegant style, not too busy, clear layout.
• Clutter, look cheap - review examples.

```html
<!DOCTYPE html>
<html lang="en">
<head>
<meta charset="utf-8">
<title>Bright Path – Flyer, Side One and Side Two</title>
<link rel="stylesheet" href="https://fonts.googleapis.com/css2?family=Poppins:wght@400;500;600;700;800&display=swap">
<style>
  :root{
    --navy:#3a4d8f;
    --navy-deep:#2f3f7c;
    --blue:#0677BA;
    --sky:#7BADD7;
    --mist:#CADEEF;
    --paper:#E8F1F8;
    --stage:#e7e8ea;
    --tick:#5fd3b5;
    --white:#ffffff;
  }
  *{box-sizing:border-box;margin:0;padding:0}
  html,body{width:1200px;height:1200px;overflow:hidden}
  body{background:var(--stage);font-family:"Poppins",sans-serif;color:var(--navy);position:relative}

  .flyer{position:absolute;top:251px;width:451px;height:697px;background:var(--paper);overflow:hidden;
    box-shadow:6px 8px 14px rgba(0,0,0,.18)}
  .flyer--front{left:125px}
  .flyer--back{left:624px}
  .abs{position:absolute}

  /* footer band */
  .contact-bar{position:absolute;left:0;bottom:0;width:100%;height:40px;background:var(--navy);
    display:flex;align-items:center;justify-content:center;gap:16px;color:var(--white);font-weight:700;font-size:13.5px}
  .contact-bar__item{display:flex;align-items:center;gap:7px}
  .contact-bar svg{width:24px;height:24px}

  /* front */
  .hero{position:absolute;left:0;top:0}
  .hero-question{position:absolute;left:43px;top:94px;font-weight:800;font-size:26px;line-height:27px;color:var(--navy);
    text-shadow:1px 1px 0 #fff,-1px -1px 0 #fff,1px -1px 0 #fff,-1px 1px 0 #fff}
  .doctor-duo{position:absolute;left:236px;top:104px;width:158px;height:158px;border-radius:50%;
    background:radial-gradient(circle at 45% 40%,#f4f6f9 0%,#dfe6ee 60%,#c9d4e1 100%);
    border:5px solid var(--white);box-shadow:0 3px 8px rgba(0,0,0,.18)}
  .wordmark{position:absolute;left:40px;top:237px;font-weight:600;font-size:24px;color:var(--navy);letter-spacing:.2px}
  .booking-title{position:absolute;left:41px;top:281px;font-weight:700;font-size:20.5px;line-height:23px;color:var(--navy)}
  .booking-title span{color:var(--blue)}
  .step-badge{position:absolute;left:41px;width:59px;height:59px;border-radius:6px;background:var(--navy);color:var(--white);
    font-weight:700;font-size:16px;line-height:19px;text-align:center;display:flex;flex-direction:column;justify-content:center}
  .step-body{position:absolute;left:122px;width:320px}
  .step-body h3{font-weight:600;font-size:14px;line-height:18px;margin-bottom:5px;color:var(--navy)}
  .checklist{list-style:none}
  .checklist li{display:flex;align-items:center;gap:6px;font-size:11.6px;line-height:15px;min-height:21px;color:var(--navy)}
  .checklist li svg{flex:0 0 16px;width:16px;height:16px}
  .checklist b{font-weight:600}

  /* back */
  .founder-photo{position:absolute;left:41px;top:41px;width:134px;height:134px;border-radius:50%;
    background:radial-gradient(circle at 50% 40%,#eef1f5 0%,#cfd8e3 70%,#b7c3d3 100%);
    border:4px solid var(--navy);box-shadow:0 0 0 3px var(--paper),0 4px 8px rgba(0,0,0,.15)}
  .founder-banner{position:absolute;left:131px;top:41px;width:280px;height:21px;background:var(--navy);color:var(--white);
    font-size:11px;line-height:21px;padding-left:64px}
  .founder-banner b{font-weight:600}
  .about{position:absolute;left:195px;top:70px;width:225px;font-size:11px;line-height:12.5px;color:var(--navy)}
  .about p+p{margin-top:12.5px}
  .section-title{position:absolute;left:41px;font-weight:600;font-size:14px;color:var(--navy)}
  .back-list{position:absolute;left:41px;width:380px}
  .back-list li{align-items:flex-start}
  .back-list li svg{margin-top:0}
  .closing{position:absolute;left:41px;top:420px;font-weight:600;font-size:11.8px;color:var(--navy)}
  .lower-wash{position:absolute;left:0;top:430px;width:100%;height:230px;background:linear-gradient(180deg,var(--paper),#f3f6fa)}
  .access-card{position:absolute;left:41px;top:455px;width:292px;height:191px;border-radius:7px;background:#f1f5fa;padding:8px;
    box-shadow:0 2px 6px rgba(0,0,0,.08)}
  .access-card__face{width:100%;height:100%;background:var(--navy);display:flex;flex-direction:column;align-items:center;justify-content:center;gap:6px}
  .access-card__name{font-weight:600;font-size:24px;color:var(--white)}
  .access-card__url{font-size:8.5px;letter-spacing:.6px;color:var(--white)}
  .physician-photo{position:absolute;left:333px;top:438px;width:118px;height:219px;
    background:linear-gradient(180deg,#eef2f6 0%,#e4e9ef 45%,#f7f8fa 100%)}
</style>
</head>
<body>

<svg width="0" height="0" style="position:absolute" aria-hidden="true">
  <symbol id="tick" viewBox="0 0 16 16">
    <circle cx="8" cy="8" r="7" fill="none" stroke="var(--tick)" stroke-width="1.1"/>
    <path d="M4.8 8.2l2.2 2.2 4.3-4.6" fill="none" stroke="var(--tick)" stroke-width="1.1" stroke-linecap="round" stroke-linejoin="round"/>
  </symbol>
  <symbol id="globe" viewBox="0 0 24 24">
    <circle cx="11" cy="11" r="9" fill="none" stroke="#fff" stroke-width="1.3"/>
    <ellipse cx="11" cy="11" rx="4" ry="9" fill="none" stroke="#fff" stroke-width="1.1"/>
    <path d="M2 11h18M3.5 6.5h15M3.5 15.5h10" fill="none" stroke="#fff" stroke-width="1.1"/>
    <path d="M15 14l7 3-3 1-1 3z" fill="#fff" stroke="var(--navy)" stroke-width=".6"/>
  </symbol>
  <symbol id="phone" viewBox="0 0 24 24">
    <circle cx="12" cy="12" r="10" fill="none" stroke="#fff" stroke-width="1.5"/>
    <path d="M6.5 15.5c1.5 1.8 3.3 3 5 3.2l1.2-1.6-1.6-1.2-.9.8c-.9-.4-1.9-1.3-2.4-2.2l.8-.9-1.2-1.6z" fill="#fff"/>
    <text x="13.5" y="11" font-family="Poppins,sans-serif" font-size="4.2" font-weight="700" fill="#fff" text-anchor="middle">CALL</text>
    <text x="14" y="15.5" font-family="Poppins,sans-serif" font-size="4.6" font-weight="800" fill="#fff" text-anchor="middle">NOW</text>
  </symbol>
</svg>

<!-- Side one -->
<section class="flyer flyer--front">
  <svg class="hero" width="451" height="205" viewBox="0 0 451 205">
    <defs>
      <linearGradient id="clinicTones" x1="0" y1="0" x2="1" y2="1">
        <stop offset="0" stop-color="#e9e6e4"/>
        <stop offset=".5" stop-color="#c9cdd6"/>
        <stop offset="1" stop-color="#8e96ac"/>
      </linearGradient>
    </defs>
    <path d="M0 0H451V152Q300 205 0 170Z" fill="url(#clinicTones)" role="img" aria-label="Photo: doctor greeting a smiling couple at a clinic desk"/>
    <path d="M0 171Q240 206 451 162V172Q280 214 0 178Z" fill="var(--navy)"/>
  </svg>
  <h1 class="hero-question">NEED<br>A DOCTOR?</h1>
  <div class="doctor-duo" role="img" aria-label="Photo: two smiling doctors in white coats"></div>

  <div class="wordmark">Bright Path</div>
  <h2 class="booking-title"><span>HOW TO BOOK</span> an Appointment<br>using your Bright Path Card</h2>

  <div class="step-badge" style="top:341px">STEP<span>1</span></div>
  <div class="step-body" style="top:339px">
    <h3>Tap Your Card on Your Phone</h3>
    <ul class="checklist">
      <li><svg><use href="#tick"/></svg>Hold your card near the back of your phone.</li>
      <li><svg><use href="#tick"/></svg>It will activate automatically — no app needed.</li>
      <li><svg><use href="#tick"/></svg>The Bright Path scheduler will open.</li>
    </ul>
  </div>

  <div class="step-badge" style="top:432px">STEP<span>2</span></div>
  <div class="step-body" style="top:430px">
    <h3>Schedule Your Appointment</h3>
    <ul class="checklist">
      <li><svg><use href="#tick"/></svg>Select your clinical concern.</li>
      <li><svg><use href="#tick"/></svg>Choose your time window.</li>
      <li><svg><use href="#tick"/></svg>Register (only once).</li>
      <li><svg><use href="#tick"/></svg>Confirm your appointment.</li>
    </ul>
  </div>

  <div class="step-badge" style="top:545px">STEP<span>3</span></div>
  <div class="step-body" style="top:542px">
    <h3>Relax, we’ll take care of the rest</h3>
    <ul class="checklist">
      <li><svg><use href="#tick"/></svg>A doctor will call during your scheduled time.</li>
      <li><svg><use href="#tick"/></svg>Once booked, you’ll be able to call our office.</li>
      <li><svg><use href="#tick"/></svg>No emails, no texts — just a real person.</li>
      <li><svg><use href="#tick"/></svg>It’s that simple.</li>
    </ul>
  </div>

  <footer class="contact-bar">
    <span class="contact-bar__item"><svg><use href="#globe"/></svg>brightpath-example.test</span>
    <span class="contact-bar__item"><svg><use href="#phone"/></svg>604 555 0142</span>
  </footer>
</section>

<!-- Side two -->
<section class="flyer flyer--back">
  <div class="lower-wash"></div>
  <div class="founder-banner">Created by <b>Dr. Marcus Ferrigan</b></div>
  <div class="founder-photo" role="img" aria-label="Photo: founding physician in a white coat with stethoscope"></div>
  <div class="about">
    <p>Bright Path was founded to make healthcare simple and convenient. Prescription renewals. Common infections. Medical notes. And so much more.</p>
    <p>Our doctors can address 120+ health concerns virtually — providing quality care without the waiting room. No waiting rooms. Just real doctors providing real care.</p>
  </div>

  <h2 class="section-title" style="top:214px">Why Patients Choose Bright Path</h2>
  <ul class="checklist back-list" style="top:240px">
    <li><svg><use href="#tick"/></svg><span><b>Easy access</b> – book and be seen from anywhere in BC.</span></li>
    <li><svg><use href="#tick"/></svg><span><b>Effortless booking</b> – tap your Bright Path Card to begin.</span></li>
    <li><svg><use href="#tick"/></svg><span><b>Trusted physicians</b> – every visit is with a licensed BC family<br>doctor.</span></li>
  </ul>

  <h2 class="section-title" style="top:315px">How It Works</h2>
  <ul class="checklist back-list" style="top:341px">
    <li><svg><use href="#tick"/></svg><span><b>Book your visit</b> — choose a time window that fits your day.</span></li>
    <li><svg><use href="#tick"/></svg><span><b>Join the queue</b> — you’ll be called when it’s your turn.</span></li>
    <li><svg><use href="#tick"/></svg><span><b>Speak directly with your doctor</b> — simple, secure, and<br>stress-free.</span></li>
  </ul>

  <p class="closing">Convenient Care for Common Concerns.</p>

  <div class="physician-photo" role="img" aria-label="Photo: smiling doctor in white coat with arms crossed"></div>
  <div class="access-card">
    <div class="access-card__face">
      <span class="access-card__name">Bright Path</span>
      <span class="access-card__url">brightpath-example.test</span>
    </div>
  </div>

  <footer class="contact-bar">
    <span class="contact-bar__item"><svg><use href="#globe"/></svg>brightpath-example.test</span>
    <span class="contact-bar__item"><svg><use href="#phone"/></svg>604 555 0142</span>
  </footer>
</section>

</body>
</html>
```